Business Card Re-Design for a Lighting Designer

I would like my business card re-designed. It is currently high gloss and they scratch too easily. I don not think the current design lends itself well to a matte finish. I have included the current design for reference along with our company logo.
Check out our website for current branding.
http://www.brambleorchidstudio.example

Updates
Some of the top contenders are muslim and it is a holiday for them. I do not want to discriminate and would expect the same courtesy for holidays we celebrate.
Target Market(s)
Interior Designers, Architects
Contact Information for Business Card
Logo - Name, Title, Address, Telephone Number and Extension, Email
Font styles to use
Requirements
Must have
- All the information listed on the current business card. If you use Red, it needs to be the red from our logo.
Nice to have
- Vertical and Horizontal Designs will be entertained.
Should not have
- Requirements for a glossy finish...should not look too corporate since we are a design firm.

```html
<!DOCTYPE html>
<html lang="en">
<head>
<meta charset="utf-8">
<title>Bramble Orchid Studio — Business Card</title>
<link rel="stylesheet" href="https://fonts.googleapis.com/css2?family=Arimo:wght@400;700&display=swap">
<style>
  :root {
    --brand-red: #b31f24;
    --brand-red-deep: #8f161b;
    --ink: #1f1f1f;
    --mute: #a9a9a9;
    --paper: #fbfbfa;
    --backdrop: #e8e5e0;
  }
  * { box-sizing: border-box; margin: 0; padding: 0; }
  html, body { width: 1200px; height: 780px; overflow: hidden; }
  body {
    background: var(--backdrop);
    font-family: "Arimo", Arial, sans-serif;
    color: var(--ink);
    position: relative;
  }
  .card {
    position: absolute;
    top: 110px;
    width: 320px;
    height: 560px;
    border-radius: 3px;
    box-shadow: 0 10px 28px rgba(0,0,0,.18);
    overflow: hidden;
  }
  .card--front { left: 230px; background: var(--paper); }
  .card--back {
    left: 650px;
    background: radial-gradient(ellipse at 40% 35%, #c8262c 0%, var(--brand-red) 45%, var(--brand-red-deep) 100%);
    color: #fff;
  }

  /* wordmark */
  .wordmark {
    display: flex;
    align-items: center;
    gap: 14px;
    justify-content: center;
  }
  .wordmark__square { width: 34px; height: 34px; background: var(--brand-red); flex: none; }
  .wordmark__name {
    font-size: 27px;
    font-weight: 400;
    line-height: 1.05;
    letter-spacing: 1px;
    color: var(--ink);
  }
  .card--front .wordmark { margin-top: 62px; }
  .wordmark--light .wordmark__square { background: #fff; }
  .wordmark--light .wordmark__name { color: #fff; font-size: 30px; }

  .person { text-align: center; margin-top: 40px; }
  .person__name { font-size: 22px; letter-spacing: 1.5px; }
  .person__title {
    font-size: 11px; letter-spacing: 5px; color: var(--mute);
    margin-top: 6px; font-weight: 700;
  }
  .address {
    text-align: center; font-size: 15px; line-height: 1.5;
    margin-top: 22px; letter-spacing: .5px;
  }

  .divider {
    display: flex; align-items: center; gap: 10px;
    margin: 18px 28px 6px;
  }
  .divider__rule { flex: 1; height: 1px; background: var(--brand-red); }
  .divider__icon {
    width: 26px; height: 26px; border-radius: 50%;
    background: var(--brand-red);
    display: flex; align-items: center; justify-content: center;
  }
  .contact { text-align: center; font-size: 15px; letter-spacing: .5px; }
  .contact--email { font-size: 13px; }

  .web-band {
    position: absolute; left: 0; right: 0; bottom: 0; height: 70px;
    background: var(--brand-red);
    color: #fff;
    display: flex; align-items: center; justify-content: center;
    font-size: 14px; letter-spacing: .6px;
  }

  .card--back .wordmark { margin-top: 210px; }
  .back-web {
    text-align: center; font-size: 13px; letter-spacing: .6px;
    margin-top: 28px; color: #fff;
  }
</style>
</head>
<body>
  <section class="card card--front" aria-label="Card front">
    <div class="wordmark">
      <span class="wordmark__square"></span>
      <span class="wordmark__name">BRAMBLE<br>ORCHID STUDIO</span>
    </div>

    <div class="person">
      <p class="person__name">MAREN COLBY</p>
      <p class="person__title">- PRINCIPAL -</p>
    </div>

    <p class="address">212 Fernhill Row<br>Suite 40 Marlow<br>Georgia 30990 USA</p>

    <div class="divider">
      <span class="divider__rule"></span>
      <span class="divider__icon">
        <svg width="14" height="14" viewBox="0 0 24 24" aria-hidden="true">
          <path fill="#fff" d="M6.6 10.8a15.1 15.1 0 0 0 6.6 6.6l2.2-2.2a1 1 0 0 1 1-.25 11.4 11.4 0 0 0 3.6.57 1 1 0 0 1 1 1V20a1 1 0 0 1-1 1A17 17 0 0 1 3 4a1 1 0 0 1 1-1h3.5a1 1 0 0 1 1 1c0 1.25.2 2.45.57 3.57a1 1 0 0 1-.25 1z"/>
        </svg>
      </span>
      <span class="divider__rule"></span>
    </div>
    <p class="contact">555.014.2280 x1</p>

    <div class="divider">
      <span class="divider__rule"></span>
      <span class="divider__icon">
        <svg width="14" height="14" viewBox="0 0 24 24" aria-hidden="true">
          <rect x="3" y="6" width="18" height="12" fill="#fff"/>
          <path d="M3 6l9 7 9-7" fill="none" stroke="#b31f24" stroke-width="1.6"/>
        </svg>
      </span>
      <span class="divider__rule"></span>
    </div>
    <p class="contact contact--email">maren@brambleorchidstudio.example</p>

    <div class="web-band">www.brambleorchidstudio.example</div>
  </section>

  <section class="card card--back" aria-label="Card back">
    <div class="wordmark wordmark--light">
      <span class="wordmark__square"></span>
      <span class="wordmark__name">BRAMBLE<br>ORCHID STUDIO</span>
    </div>
    <p class="back-web">www.brambleorchidstudio.example</p>
  </section>
</body>
</html>
```